Startup photography business has a new logo, now we need business cards

Design a business card for the two partners of our business.
Our business Brisk Pelican has a new logo and we need to design a business card to showcase it and us.
Our colours of blue and orange are punchy and vivid, but how can we make the most of it on our card?

It should have our name Brisk Pelican
name of partner
phone number
email
website

Industry/Entity Type

Professional Photography

Contact Information for Business Card

Tom Ashworth
+61 400 55 61 72
tom@briskpelican.com.au
briskpelican.com.au

second card
Neil Porter
+61 400 918 263
neil@briskpelican.com.au
briskpelican.com.au

Colors
f37122
f68d4c
33a6d7
0592cd

Requirements
Must have
• one version of our logo, we have included options
• Name
• phone number
• email
• website
Nice to have
• instagram briskpelicanmedia
• twitter briskpelicanmedia
• facebook briskpelicanmedia

```html
<!DOCTYPE html>
<html lang="en">
<head>
<meta charset="utf-8">
<title>Brisk Pelican – Business Card</title>
<link rel="stylesheet" href="https://fonts.googleapis.com/css2?family=Source+Sans+3:wght@400;600;700&display=swap">
<style>
  :root {
    --page-bg: #dcdfe2;
    --card-frost: #eef2f4;
    --brand-blue: #0592cd;
    --brand-blue-light: #33a6d7;
    --brand-blue-top: #45b6e6;
    --brand-orange: #f37122;
    --text-light: #f4fbff;
    --text-soft: #d9f0fb;
  }
  * { margin: 0; padding: 0; box-sizing: border-box; }
  html, body {
    width: 1200px; height: 969px; overflow: hidden;
    background: var(--page-bg);
    font-family: "Source Sans 3", "Segoe UI", sans-serif;
  }
  .canvas { position: relative; width: 1200px; height: 969px; }
  .business-card {
    position: absolute; left: 100px; top: 222px;
    width: 1000px; height: 524px;
    border-radius: 26px; overflow: hidden;
    background: var(--card-frost);
    box-shadow: 0 10px 30px rgba(0,0,0,0.12);
  }
  .card-shapes { position: absolute; inset: 0; width: 100%; height: 100%; }
  .partner-name {
    position: absolute; left: 52px; top: 122px;
    font-size: 33px; font-weight: 600; letter-spacing: 0.5px;
    color: var(--text-light); text-transform: uppercase;
  }
  .contact-list { position: absolute; left: 52px; top: 186px; list-style: none; }
  .contact-item {
    display: flex; align-items: center; gap: 18px;
    height: 44px; font-size: 25px; color: var(--text-light);
  }
  .contact-icon { width: 22px; height: 22px; flex: none; }
  .social-row { position: absolute; left: 52px; top: 344px; display: flex; gap: 10px; }
  .social-dot {
    width: 44px; height: 44px; border-radius: 50%;
    border: 2px solid var(--text-soft);
  }
  .social-handle {
    position: absolute; left: 52px; top: 400px;
    font-size: 25px; color: var(--text-soft);
  }
  .brand-name {
    position: absolute; left: 600px; top: 338px; width: 330px;
    text-align: center; font-size: 46px; font-weight: 700;
    color: var(--brand-blue); text-transform: uppercase; letter-spacing: 1px;
  }
</style>
</head>
<body>
<main class="canvas">
  <section class="business-card">
    <svg class="card-shapes" viewBox="0 0 1000 524" preserveAspectRatio="none" aria-hidden="true">
      <defs>
        <linearGradient id="panelBlue" x1="0" y1="0" x2="0.3" y2="1">
          <stop offset="0" stop-color="var(--brand-blue-top)"/>
          <stop offset="1" stop-color="var(--brand-blue)"/>
        </linearGradient>
      </defs>
      <path class="blue-panel" d="M0 0 H522 Q430 262 546 524 H0 Z" fill="url(#panelBlue)"/>
      <path class="orange-arc" d="M536 0 Q446 262 560 524" fill="none" stroke="var(--brand-orange)" stroke-width="9"/>
    </svg>

    <h1 class="partner-name">Tom Ashworth</h1>

    <ul class="contact-list">
      <li class="contact-item">
        <svg class="contact-icon" viewBox="0 0 24 24"><path fill="var(--text-soft)" d="M6.6 10.8a15.2 15.2 0 0 0 6.6 6.6l2.2-2.2a1 1 0 0 1 1-.25 11.4 11.4 0 0 0 3.6.57 1 1 0 0 1 1 1V20a1 1 0 0 1-1 1A17 17 0 0 1 3 4a1 1 0 0 1 1-1h3.5a1 1 0 0 1 1 1c0 1.25.2 2.45.57 3.57a1 1 0 0 1-.25 1z"/></svg>
        <span>+61 400 55 61 72</span>
      </li>
      <li class="contact-item">
        <svg class="contact-icon" viewBox="0 0 24 24"><rect x="2" y="5" width="20" height="14" rx="1.5" fill="var(--text-soft)"/><path d="M3 6l9 7 9-7" fill="none" stroke="var(--brand-blue)" stroke-width="1.6"/></svg>
        <span>tom@briskpelican.com.au</span>
      </li>
      <li class="contact-item">
        <svg class="contact-icon" viewBox="0 0 24 24"><circle cx="12" cy="12" r="10" fill="none" stroke="var(--text-soft)" stroke-width="2"/><path d="M2 12h20M12 2c3 3 3 17 0 20M12 2c-3 3-3 17 0 20" fill="none" stroke="var(--text-soft)" stroke-width="1.6"/></svg>
        <span>www.briskpelican.com.au</span>
      </li>
    </ul>

    <div class="social-row" aria-hidden="true">
      <span class="social-dot"></span>
      <span class="social-dot"></span>
      <span class="social-dot"></span>
    </div>
    <p class="social-handle">briskpelicanmedia</p>

    <p class="brand-name">Brisk Pelican</p>
  </section>
</main>
</body>
</html>
```